Cleaners Needs Bounce-Back Coupon For Laundry Service

We need a "bounce-back" coupon to attach to peoples dry cleaning orders that offers one free wash-n-fold laundry service. Right now we always attach their receipt to the bag that contains their dry cleaning when we return it. We'd like to also attach a coupon that will entice them to come try our laundry service.

Background on the service: We sort, wash, dry, and fold the laundry for customers and then neatly put it in a nice bag that makes returning very convenient. Their laundry comes out fresh, clean, smelling great, and without the hassle of doing it themselves. We have a great return rate. Most customers that try out the service become long term customers. The goal is to get our dry cleaning customers to come try it out.

Requirements:
* 5" x 8" and one-sided.
* To be printed on a standard color of card stock.
* Must incorporate our logo.
* Needs a place for us to fill in an expiration date. We'll fill in a date about two weeks out from the time they pick up their dry cleaning.
* Limit one coupon per customer.
* Limit 50 pounds of laundry per coupon.

Industry/Entity Type

Dry Cleaning

```html
<!DOCTYPE html>
<html lang="en">
<head>
<meta charset="utf-8">
<title>Bounce-Back Coupon</title>
<link href="https://fonts.googleapis.com/css2?family=Lato:wght@400;700;900&family=Oswald:wght@500&display=swap" rel="stylesheet">
<style>
:root{
  --orange:#ff6a00;
  --blue:#0a3a9e;
  --blue-dark:#06287a;
  --grey-bg:#e9e9ea;
  --grey-text:#4a4a4a;
  --white:#ffffff;
}
*{margin:0;padding:0;box-sizing:border-box}
html,body{width:844px;height:1200px;overflow:hidden;background:var(--white)}
.coupon{position:relative;width:844px;height:1200px;overflow:hidden;
  background:radial-gradient(circle at 50% 48%, #ffffff 0%, #f1f1f2 45%, #d9d9db 100%);
  font-family:"Lato",sans-serif}
.shapes{position:absolute;inset:0;width:844px;height:1200px}
.brand-box{position:absolute;left:123px;top:0;width:574px;height:194px;background:var(--white);
  border-radius:0 0 28px 28px;display:flex;align-items:center;justify-content:center;gap:18px;
  box-shadow:0 4px 10px rgba(0,0,0,.18)}
.brand-mark{width:26px;height:26px;border-radius:50%;background:var(--blue)}
.brand-name{font-family:"Lato",sans-serif;font-weight:700;font-size:58px;color:var(--blue)}
.photo{position:absolute;left:236px;top:331px;width:368px;height:368px;border-radius:50%;
  background:linear-gradient(135deg,#c9ccd1 0%,#9aa0a8 40%,#c1272d 62%,#e8e8e8 100%)}
.limit{position:absolute;font-family:"Oswald",sans-serif;font-weight:500;font-size:27px;
  color:var(--blue);letter-spacing:.5px;white-space:nowrap;top:588px;
  transform:translate(-50%,-50%) rotate(-90deg)}
.limit-left{left:54px}
.limit-right{left:800px}
.offer-pill{position:absolute;left:183px;top:829px;width:472px;height:58px;border-radius:29px;
  background:linear-gradient(#ff8a2a,var(--orange));color:var(--white);font-weight:700;
  font-size:44px;display:flex;align-items:center;justify-content:center;
  box-shadow:0 3px 6px rgba(0,0,0,.2)}
.details{position:absolute;left:60px;right:60px;top:906px;text-align:center}
.details h2{color:var(--blue);font-weight:700;font-size:19.5px;margin-bottom:6px}
.details p{color:var(--grey-text);font-weight:700;font-size:17.5px;line-height:23px}
.details h3{color:var(--blue);font-weight:700;font-size:19.5px;margin-top:5px}
.details .goal{font-weight:400;color:#333}
.expiry-box{position:absolute;left:188px;top:1126px;width:456px;height:90px;background:var(--white);
  border-radius:30px 30px 0 0}
</style>
</head>
<body>
<div class="coupon">
  <svg class="shapes" viewBox="0 0 844 1200" aria-hidden="true">
    <path d="M0 0H844V250Q422 330 0 250Z" fill="var(--orange)"/>
    <path d="M0 262Q422 342 844 262" fill="none" stroke="var(--white)" stroke-width="14"/>
    <path d="M0 280Q422 360 844 280" fill="none" stroke="var(--blue)" stroke-width="20"/>
    <path d="M166 423A270 270 0 0 1 674 423" fill="none" stroke="var(--blue)" stroke-width="24"/>
    <path d="M166 607A270 270 0 0 0 674 607" fill="none" stroke="var(--blue)" stroke-width="24"/>
    <rect x="636" y="426" width="86" height="74" fill="var(--orange)"/>
    <rect x="636" y="514" width="86" height="74" fill="var(--orange)"/>
    <circle cx="420" cy="515" r="224" fill="var(--orange)"/>
    <circle cx="420" cy="515" r="209" fill="none" stroke="var(--white)" stroke-width="3" stroke-dasharray="9 6"/>
    <circle cx="420" cy="515" r="198" fill="var(--blue)"/>
    <path d="M0 1070Q422 1040 844 1070" fill="none" stroke="var(--orange)" stroke-width="8"/>
    <path d="M0 1082Q422 1052 844 1082V1200H0Z" fill="var(--blue)"/>
  </svg>

  <header class="brand-box">
    <span class="brand-mark"></span>
    <span class="brand-name">Fold &amp; Fresh</span>
  </header>

  <div class="photo" role="img" aria-label="Photo of a smiling laundry attendant holding a white laundry basket in front of washing machines"></div>

  <div class="limit limit-left">LIMIT ONE COUPON PER CUSTOMER</div>
  <div class="limit limit-right">LIMIT 50 POUNDS OF LAUNDRY PER COUPON</div>

  <div class="offer-pill">Bounce-Back</div>

  <section class="details">
    <h2>DRYCLEANING THAT OFFERS ONE FREE WASH-N-FOLD LAUNDRY SERVICE</h2>
    <p>We sort, wash, dry, and fold the laundry for customers and then neatly put it in a nice bag that makes returning very convenient.The laundry results comes out fresh, clean, smelling great and hasslefree.We have a great return rate which allows longterm customers</p>
    <h3>OUR GOAL:</h3>
    <p class="goal">To get our dry cleaning customers to come and try it out</p>
  </section>

  <div class="expiry-box"></div>
</div>
</body>
</html>
```